Brass Kettle Business Card

I needed some business cards done for my band. We are a 9 piece funk/horn band that plays a lot of private parties, wedding receptions and music festivals. We'd like a design with vivid colors that incorporates our logo. You can check out our website at www.brasskettleband.com to see what type of vibe we are going for.

```html
<!DOCTYPE html>
<html lang="en">
<head>
<meta charset="utf-8">
<title>Brass Kettle Business Card</title>
<link rel="stylesheet" href="https://fonts.googleapis.com/css2?family=Bebas+Neue&family=Montserrat:wght@400;500;700;800&display=swap">
<style>
  :root {
    --lime: #c8e62a;
    --white: #ffffff;
    --ink: #120a09;
    --card-dark: #140b0d;
    --back-dark: #1b1819;
    --purple: #6a1f8a;
    --violet: #3a1a9a;
    --magenta: #a8247e;
    --paper: #ffffff;
  }
  * { box-sizing: border-box; margin: 0; padding: 0; }
  html, body { width: 1200px; height: 1200px; overflow: hidden; }
  body { position: relative; background: var(--paper); font-family: "Montserrat", sans-serif; }

  .stage { position: absolute; left: 0; width: 1200px; height: 600px; }
  .stage--light { top: 0; background: var(--paper); }
  .stage--dark { top: 600px; background: var(--ink); }

  .card {
    position: absolute; top: 188px; width: 391px; height: 223px; overflow: hidden;
  }
  .stage--light .card { box-shadow: 6px 8px 12px rgba(0,0,0,0.22); }
  .card--front { left: 185px; background: var(--card-dark); }
  .card--back { left: 650px; background: var(--back-dark); }

  .stage-photo {
    position: absolute; left: 0; top: 0; width: 260px; height: 223px;
    background:
      radial-gradient(ellipse at 30% 25%, rgba(90,40,200,0.9), transparent 60%),
      radial-gradient(ellipse at 45% 55%, var(--magenta), transparent 65%),
      linear-gradient(180deg, var(--violet) 0%, var(--purple) 60%, #3a0f3f 100%);
    -webkit-mask-image: linear-gradient(90deg, #000 55%, transparent 100%);
    mask-image: linear-gradient(90deg, #000 55%, transparent 100%);
  }
  .drum-photo {
    position: absolute; inset: 0;
    background:
      radial-gradient(ellipse at 55% 70%, #4a4647 0%, #2c292a 40%, transparent 70%),
      linear-gradient(160deg, #121011 0%, #221f20 60%, #2a2728 100%);
  }

  .corner {
    position: absolute; left: 353px; top: 14px; width: 23px; height: 23px;
    border-top: 2px solid var(--white); border-right: 2px solid var(--white);
  }
  .corner--lime { border-color: var(--lime); }

  .rule-pair { position: absolute; left: 0; width: 43px; height: 12px; top: 196px;
    border-top: 2px solid var(--white); border-bottom: 2px solid var(--white); }
  .rule-pair--lime { border-color: var(--lime); }

  .brand-name {
    position: absolute; color: var(--lime); font-weight: 800; white-space: nowrap;
    transform: translate(-50%, -50%); letter-spacing: 0.2px;
  }
  .card--front .brand-name { left: 100px; top: 110px; font-size: 21px; }
  .card--back .brand-name { left: 195px; top: 102px; font-size: 33px; }

  .tagline {
    position: absolute; right: 45px; top: 39px; text-align: right;
    font-family: "Bebas Neue", sans-serif; color: var(--lime);
    font-size: 13.5px; line-height: 15.5px; letter-spacing: 1.6px;
  }

  .contact { position: absolute; left: 238px; top: 92px; color: var(--white); }
  .contact__title { font-weight: 700; font-size: 10.5px; letter-spacing: 0.3px; }
  .contact__note { font-size: 6px; letter-spacing: 0.3px; margin-top: 1px; }

  .contact-list { position: absolute; left: 219px; top: 130px; list-style: none; }
  .contact-list li {
    display: flex; align-items: center; height: 16px;
    color: var(--white); font-size: 9px; font-weight: 500;
  }
  .contact-list svg { width: 11px; height: 11px; margin-right: 8px; flex: none; }

  .social { position: absolute; left: 238px; top: 196px; display: flex; align-items: center;
    color: var(--white); font-size: 9px; font-weight: 500; }
  .social__dot { width: 10px; height: 10px; border: 1px solid var(--white); border-radius: 50%; margin-right: 6px; }

  .web-address {
    position: absolute; left: 0; width: 100%; top: 165px; text-align: center;
    font-family: "Bebas Neue", sans-serif; color: var(--white);
    font-size: 12px; letter-spacing: 4.2px;
  }
</style>
</head>
<body>

<section class="stage stage--light">
  <article class="card card--front">
    <div class="stage-photo" role="img" aria-label="Band singer performing on a purple-lit stage with a drum kit behind"></div>
    <div class="corner"></div>
    <div class="rule-pair"></div>
    <div class="brand-name">Brass Kettle</div>
    <p class="tagline">Where the soul<br>meets the groove</p>
    <div class="contact">
      <p class="contact__title">CONTACT US</p>
      <p class="contact__note">TO BOOK BRASS KETTLE CALL OR EMAIL</p>
    </div>
    <ul class="contact-list">
      <li><svg viewBox="0 0 12 12"><circle cx="6" cy="6" r="6" fill="var(--lime)"/><path d="M4 3.2l1 1.2-.6.8c.4.9 1 1.5 1.9 1.9l.8-.6 1.2 1-.6 1c-2.4-.3-4.3-2.2-4.6-4.6z" fill="var(--card-dark)"/></svg>555 014 2286</li>
      <li><svg viewBox="0 0 12 12"><circle cx="6" cy="6" r="6" fill="var(--lime)"/><rect x="3.2" y="4" width="5.6" height="4" fill="none" stroke="var(--card-dark)" stroke-width=".8"/><path d="M3.2 4l2.8 2.2L8.8 4" fill="none" stroke="var(--card-dark)" stroke-width=".8"/></svg>info@brasskettleband.com</li>
      <li><svg viewBox="0 0 12 12"><circle cx="6" cy="6" r="6" fill="var(--lime)"/><circle cx="6" cy="6" r="3" fill="none" stroke="var(--card-dark)" stroke-width=".7"/><path d="M3 6h6M6 3c-1.3 1.7-1.3 4.3 0 6M6 3c1.3 1.7 1.3 4.3 0 6" fill="none" stroke="var(--card-dark)" stroke-width=".6"/></svg>www.brasskettleband.com</li>
    </ul>
    <div class="social"><span class="social__dot"></span>brasskettleband</div>
  </article>

  <article class="card card--back">
    <div class="drum-photo" role="img" aria-label="Dim black and white close-up of a conga drum"></div>
    <div class="corner corner--lime"></div>
    <div class="rule-pair rule-pair--lime"></div>
    <div class="brand-name">Brass Kettle</div>
    <p class="web-address">WWW.BRASSKETTLEBAND.COM</p>
  </article>
</section>

<section class="stage stage--dark">
  <article class="card card--front">
    <div class="stage-photo" role="img" aria-label="Band singer performing on a purple-lit stage with a drum kit behind"></div>
    <div class="corner"></div>
    <div class="rule-pair"></div>
    <div class="brand-name">Brass Kettle</div>
    <p class="tagline">Where the soul<br>meets the groove</p>
    <div class="contact">
      <p class="contact__title">CONTACT US</p>
      <p class="contact__note">TO BOOK BRASS KETTLE CALL OR EMAIL</p>
    </div>
    <ul class="contact-list">
      <li><svg viewBox="0 0 12 12"><circle cx="6" cy="6" r="6" fill="var(--lime)"/><path d="M4 3.2l1 1.2-.6.8c.4.9 1 1.5 1.9 1.9l.8-.6 1.2 1-.6 1c-2.4-.3-4.3-2.2-4.6-4.6z" fill="var(--card-dark)"/></svg>555 014 2286</li>
      <li><svg viewBox="0 0 12 12"><circle cx="6" cy="6" r="6" fill="var(--lime)"/><rect x="3.2" y="4" width="5.6" height="4" fill="none" stroke="var(--card-dark)" stroke-width=".8"/><path d="M3.2 4l2.8 2.2L8.8 4" fill="none" stroke="var(--card-dark)" stroke-width=".8"/></svg>info@brasskettleband.com</li>
      <li><svg viewBox="0 0 12 12"><circle cx="6" cy="6" r="6" fill="var(--lime)"/><circle cx="6" cy="6" r="3" fill="none" stroke="var(--card-dark)" stroke-width=".7"/><path d="M3 6h6M6 3c-1.3 1.7-1.3 4.3 0 6M6 3c1.3 1.7 1.3 4.3 0 6" fill="none" stroke="var(--card-dark)" stroke-width=".6"/></svg>www.brasskettleband.com</li>
    </ul>
    <div class="social"><span class="social__dot"></span>brasskettleband</div>
  </article>

  <article class="card card--back">
    <div class="drum-photo" role="img" aria-label="Dim black and white close-up of a conga drum"></div>
    <div class="corner corner--lime"></div>
    <div class="rule-pair rule-pair--lime"></div>
    <div class="brand-name">Brass Kettle</div>
    <p class="web-address">WWW.BRASSKETTLEBAND.COM</p>
  </article>
</section>

</body>
</html>
```